Hollowbrook Yard Services - Needs a business card! Easy JOB!

I need a business card for a new company called Hollowbrook Yard Services. I will be offering the below services.

I am relatively open for ideas, so please be at your creative best.

I think I will list all the services offered on the rear of the card.

- Gardening
- Lawn Care
- Hedge Trimming
- Rubbish Removal
- Weeding/Spraying
- Landscaping
- Gutter Cleaning
- Solar Panel Cleaning
- Irrigation
- Pruning
- On-Site Mulching
- Ask for other services

I am still a little undecided on the colours. I prefer the logos with the Blue text, but I am open for ideas ( the logo/texts colours are not final).

Please use the catch phrase "What can Hollowbrook do for you?"

Here are the required details.

Hollowbrook Yard Services

Miles Fenwarick (owner)
Ph: 1300 555 014
Mob: 0400 555 286

miles@hollowbrookyard.com.au
www.hollowbrookyard.com.au
facebook.com/HollowbrookYard
twitter.com/HollowbrookYard
ABN: 555 019 472 ( this can be in smaller text somewhere, this is the least important )

Thankyou in advance! And good luck.

regards,
Miles
Updates

Hi everyone, please make sure you include the phrase "What can Hollowbrook do for you?" on the designs.

thanks,
Miles

Definitely liking the focus on a majority of the design on the blue colour from the logo. Also a splash of green in the plant.

Please make sure you list the services provided on the rear of the card. thanks.

With the service listing, please make "ask for other services" stand out, either a different colour or position or size... as long as it is more noticeable than the other services listed. Thanks.

Industry/Entity Type

Business

Requirements
Must have
• - use the font supplied (Brandon Family Font)
- use of the catch phrase "What can Hollowbrook do for you?"
- Double sided design
- Chatterly and Quipster logos/links
- Please use symbol/picture for "phone" "mobile" "email" instead of using the words.
- List the services provided on the rear of the card

```html
<!DOCTYPE html>
<html lang="en">
<head>
<meta charset="utf-8">
<title>Hollowbrook Yard Services – Business Card</title>
<link rel="stylesheet" href="https://fonts.googleapis.com/css2?family=Open+Sans:wght@300;400;700&family=Dancing+Script:wght@500&display=swap">
<style>
  :root {
    --leaf: #3e7b1f;
    --leaf-dark: #2f6314;
    --leaf-faint: #4f8a30;
    --leaf-edge: #8fb878;
    --paper: #f7f7f5;
    --ink: #3b3f3a;
    --muted: #a9aca6;
    --backdrop: #dcdcd8;
  }
  * { box-sizing: border-box; margin: 0; padding: 0; }
  html, body { width: 1200px; height: 675px; overflow: hidden; }
  body {
    background: var(--backdrop);
    font-family: "Open Sans", Arial, sans-serif;
    position: relative;
  }
  .card {
    position: absolute;
    top: 172px;
    width: 540px;
    height: 330px;
    background: var(--paper);
    overflow: hidden;
    box-shadow: 0 6px 18px rgba(0,0,0,.18);
  }
  .card--front { left: 40px; }
  .card--back { left: 620px; }

  .band { position: absolute; left: 0; top: 0; width: 540px; background: var(--leaf); }
  .band-edge {
    position: absolute; left: 0; width: 540px; height: 18px;
    background: linear-gradient(to bottom, var(--leaf) 0%, var(--leaf-edge) 55%, var(--paper) 100%);
  }

  /* front */
  .card--front .band { height: 40px; }
  .card--front .band-edge { top: 40px; }
  .grass-strip {
    position: absolute; left: 0; top: 70px; width: 540px; height: 160px;
    background: linear-gradient(to bottom, rgba(120,190,70,0) 0%, rgba(110,180,60,.55) 35%, #5aa12c 70%, #3e7b1f 100%);
  }
  .brand-title {
    position: absolute; left: 0; width: 540px; top: 128px;
    text-align: center; font-size: 31px; font-weight: 300; color: var(--ink);
    letter-spacing: -0.3px;
  }
  .brand-title strong { font-weight: 700; color: var(--leaf-dark); }
  .tagline {
    position: absolute; right: 22px; bottom: 18px;
    font-family: "Dancing Script", cursive; font-size: 17px; color: var(--ink);
  }

  /* back */
  .card--back .band { height: 192px; }
  .card--back .band-edge { top: 192px; }
  .contact { position: absolute; left: 22px; top: 14px; color: #fff; font-size: 12.5px; line-height: 17px; }
  .contact .web { font-size: 17px; font-weight: 300; margin-bottom: 3px; }
  .contact .web b { font-weight: 700; }
  .contact-list { list-style: none; }
  .contact-list li { display: flex; align-items: center; gap: 6px; }
  .contact-list svg { width: 12px; height: 12px; flex: none; }
  .abn { position: absolute; right: 12px; top: 14px; color: #fff; font-size: 8px; }
  .abn b { font-weight: 700; }
  .person { position: absolute; left: 110px; top: 114px; color: #fff; font-size: 34px; font-weight: 300; }
  .person b { font-weight: 700; }
  .ask { position: absolute; left: 110px; top: 218px; color: var(--leaf-faint); font-size: 12.5px; font-weight: 700; }
  .role { position: absolute; left: 270px; top: 228px; color: var(--leaf); font-size: 30px; font-weight: 700; }
  .social { position: absolute; left: 22px; bottom: 16px; color: var(--leaf); font-size: 12.5px; line-height: 16px; font-weight: 300; }
  .social b { font-weight: 700; }
  .service { position: absolute; white-space: nowrap; color: var(--muted); font-weight: 400; }
  .service--on-band { color: var(--leaf-faint); }
</style>
</head>
<body>

<section class="card card--front" aria-label="Card front">
  <div class="band"></div>
  <div class="band-edge" role="img" aria-label="Zigzag grass-edge border"></div>
  <div class="grass-strip" role="img" aria-label="Photo of a strip of fresh green grass blades"></div>
  <h1 class="brand-title">Hollowbrook <strong>Yard</strong> Services</h1>
  <p class="tagline">What can Hollowbrook do for you?</p>
</section>

<section class="card card--back" aria-label="Card back">
  <div class="band"></div>
  <div class="band-edge" role="img" aria-label="Zigzag grass-edge border"></div>

  <span class="service service--on-band" style="left:420px;top:36px;font-size:10px;transform:rotate(12deg)">On-Site Mulching</span>
  <span class="service service--on-band" style="left:330px;top:58px;font-size:10px;transform:rotate(18deg)">Hedge Trimming</span>
  <span class="service service--on-band" style="left:445px;top:74px;font-size:15px;transform:rotate(10deg)">Gardening</span>
  <span class="service service--on-band" style="left:232px;top:96px;font-size:12px">Weeding/Spraying</span>
  <span class="service service--on-band" style="left:372px;top:100px;font-size:14px;transform:rotate(22deg)">Irrigation</span>
  <span class="service service--on-band" style="left:470px;top:150px;font-size:14px;transform:rotate(-22deg)">Pruning</span>

  <div class="contact">
    <p class="web">www.<b>HollowbrookYard</b>.com.au</p>
    <ul class="contact-list">
      <li><svg viewBox="0 0 24 24" aria-label="Phone"><path fill="#fff" d="M6.6 10.8a15.1 15.1 0 0 0 6.6 6.6l2.2-2.2a1 1 0 0 1 1-.25 11.4 11.4 0 0 0 3.6.57 1 1 0 0 1 1 1V20a1 1 0 0 1-1 1A17 17 0 0 1 3 4a1 1 0 0 1 1-1h3.5a1 1 0 0 1 1 1c0 1.25.2 2.45.57 3.57a1 1 0 0 1-.25 1z"/></svg>1300 555 014</li>
      <li><svg viewBox="0 0 24 24" aria-label="Mobile"><rect x="6" y="1.5" width="12" height="21" rx="2" fill="none" stroke="#fff" stroke-width="2.2"/><circle cx="12" cy="18.5" r="1.3" fill="#fff"/></svg>0400 555 286</li>
      <li><svg viewBox="0 0 24 24" aria-label="Email"><rect x="2" y="5" width="20" height="14" rx="1.5" fill="none" stroke="#fff" stroke-width="2.2"/><path d="M2.5 6l9.5 7 9.5-7" fill="none" stroke="#fff" stroke-width="2.2"/></svg>miles@hollowbrookyard.com.au</li>
    </ul>
  </div>
  <p class="abn"><b>ABN:</b> 555 019 472</p>
  <h2 class="person">Miles <b>Fenwarick</b></h2>

  <p class="ask">Ask for other services</p>
  <p class="role">Owner</p>

  <span class="service" style="left:455px;top:222px;font-size:15px;transform:rotate(28deg)">Lawn Care</span>
  <span class="service" style="left:262px;top:276px;font-size:9px;transform:rotate(-8deg)">Solar Panel Cleaning</span>
  <span class="service" style="left:392px;top:256px;font-size:9px;transform:rotate(-28deg)">Landscaping</span>
  <span class="service" style="left:300px;top:296px;font-size:13px;transform:rotate(-16deg)">Gutter Cleaning</span>
  <span class="service" style="left:420px;top:290px;font-size:12px;transform:rotate(22deg)">Rubbish Removal</span>

  <p class="social">facebook.com/<b>HollowbrookYard</b><br>twitter.com/<b>HollowbrookYard</b></p>
</section>

</body>
</html>
```